Pill Empires and the Decay of Healing: What Every Patient Should See

brindlemart lumen pub and print on demand. Here are similar books with terrible covers: https://www.brindlemart.example/Fatal-Remedies-Hidden-Racket-Clinics/dp/5512093377
https://www.brindlemart.example/Anxious-Patient-Refill-Overdiagnosed-Nation/dp/5512093385
https://www.brindlemart.example/Crooked-Tablets-Firms-Deceive-Clinicians/dp/5512093393
https://www.brindlemart.example/s/?ie=UTF8&keywords=dosefall&tag=srchlnk-20&index=aps&hvadid=504219837761&hvpos=1t1&hvnetw=g&hvrand=60427719385042277163&hvpone=&hvptwo=&hvqmt=e&hvdev=c&hvdvcmdl=&hvlocint=&hvlocphy=4470288&hvtargid=kwd-73018845521&ref=pd_sl_4k208tqrab_e
https://www.brindlemart.example/Overloaded-Wards-Pledge-Western-Healing/dp/5512093407
https://www.brindlemart.example/Snared-Vocation-Chemical-Inquiries-Liberal-Arts/dp/5512093415
https://www.brindlemart.example/dp/Q77R3K9M2T/ref=dp-lumen-redirect?_encoding=UTF8&btkr=1
https://www.brindlemart.example/Sultans-Bare-Pills-Cracking-Mood-Tablet/dp/5512093423
https://www.brindlemart.example/Lethal-Asylum-Planned-Silence-Varnholt-ebook/dp/Q82V5L1N4W

Help! you can do better than this!

Sick

Target Market(s)

medical readers science readers

Colors

Designer to choose colors to be used in the design.

Requirements
Must have
• great eye catching cover here is excerpt
• As my insight grew, I discovered patient after patient who was broken on the torture-wheel of our therapies, their lives ruined by toxic drugs or surgery. I saw men with back pain which likely would have been self-limited turned into struggling opioid addicts by our promiscuous prescribing culture. Some had surgery supported by no more science than a bar stabbing. I saw people taking ten or more prescriptions. I saw depression and intellectual decline with statin and beta blocker combinations. I saw irreversible brain damage from psychiatric drugs. I saw a lot more.
• As I learned, I felt obliged to share my discoveries, so I began to write. I will take you through my journey step by step. I use quotes, links, and explanatory footnotes liberally to make authentication easy. As you start to grasp the tragedy, you will realize why I cannot sugar-coat or use euphemisms.
Nice to have
• reasonable dignity (no gravestones) but this is a serious subject
• it's freaking a terrible situation
• hope you can do better than the other examples

```html
<!DOCTYPE html>
<html lang="en">
<head>
<meta charset="utf-8">
<title>Pill Empires and the Decay of Healing — Book Cover</title>
<link rel="stylesheet" href="https://fonts.googleapis.com/css2?family=Bebas+Neue&family=Oswald:wght@300;400&family=Lato:wght@400&display=swap">
<style>
  :root {
    --ink: #000000;
    --serpent-blue: #346699;
    --serpent-deep: #2a5582;
    --paper: #ffffff;
  }
  * { margin: 0; padding: 0; box-sizing: border-box; }
  html, body {
    width: 800px;
    height: 1200px;
    overflow: hidden;
    background: var(--ink);
  }
  .cover {
    position: relative;
    width: 800px;
    height: 1200px;
    background: var(--ink);
    overflow: hidden;
  }
  .emblem-area {
    position: absolute;
    left: 0;
    top: 0;
    width: 800px;
    height: 1200px;
  }
  .title {
    position: absolute;
    left: 0;
    top: 336px;
    width: 800px;
    text-align: center;
    font-family: "Bebas Neue", "Oswald", sans-serif;
    font-weight: 400;
    font-size: 142px;
    line-height: 132px;
    color: var(--paper);
    letter-spacing: 0.5px;
  }
  .title .line { display: block; }
  .subtitle {
    position: absolute;
    left: 0;
    top: 960px;
    width: 800px;
    text-align: center;
    font-family: "Oswald", sans-serif;
    font-weight: 300;
    font-size: 38px;
    color: var(--paper);
    letter-spacing: 0.5px;
  }
  .author {
    position: absolute;
    left: 0;
    top: 1098px;
    width: 800px;
    text-align: center;
    font-family: "Lato", sans-serif;
    font-weight: 400;
    font-size: 42px;
    color: var(--paper);
    letter-spacing: -0.5px;
  }
</style>
</head>
<body>
  <main class="cover">
    <svg class="emblem-area" viewBox="0 0 800 1200" role="img" aria-label="Large blue serpent coiled around a staff, rising diagonally from the lower right to the upper left of the cover">
      <defs>
        <linearGradient id="serpentTone" x1="0" y1="0" x2="1" y2="1">
          <stop offset="0%" stop-color="var(--serpent-blue)"/>
          <stop offset="100%" stop-color="var(--serpent-deep)"/>
        </linearGradient>
      </defs>
      <rect class="emblem-fill" x="-190" y="-640" width="380" height="1320" rx="190"
            fill="url(#serpentTone)" transform="translate(400 600) rotate(-30)"/>
    </svg>

    <h1 class="title">
      <span class="line">Pill Empires</span>
      <span class="line">And the</span>
      <span class="line">Decay of</span>
      <span class="line">Healing</span>
    </h1>

    <p class="subtitle">What Every Patient Should See</p>

    <p class="author">DANIEL MARSH</p>
  </main>
</body>
</html>
```